Limbwright Crew of Yuma Bill Board Design

We are a high class full service tree company who specializes in artistic thinning and shaping of trees in Arizona. We want to re brand our company to catch our audiences attention and hook them into calling our company on the spot. We’ve been in business for 30 years and have never truly branded our company. We want our shirts trucks and billboards to match as well as our mailing advertisement so our clientele can recognize us immediately. We are starting with our billboard first and will be following with truck and shirt designs next. Attached is a example of what we are looking for and what we’ve had designed so far. This just isn’t good enough and needs revamped if at all posssible.
- Stencil

```html
<!DOCTYPE html>
<html lang="en">
<head>
<meta charset="utf-8">
<title>Limbwright Crew of Yuma Billboard</title>
<link rel="stylesheet" href="https://fonts.googleapis.com/css2?family=Kaushan+Script&family=Montserrat:ital,wght@0,300;0,700;1,400&display=swap">
<style>
  :root {
    --stage: #2c3f6e;
    --board-white: #f1f2f3;
    --green-deep: #127b3d;
    --green-bright: #30b653;
    --photo-tone-a: #8fb27a;
    --photo-tone-b: #a9a658;
    --ink: #16181c;
    --text-light: #ffffff;
  }
  html, body {
    margin: 0;
    padding: 0;
    width: 1200px;
    height: 900px;
    overflow: hidden;
    background: var(--stage);
  }
  .billboard {
    position: absolute;
    left: 40px;
    top: 174px;
    width: 1120px;
    height: 551px;
    display: block;
  }
  .board-base { fill: var(--board-white); }
  .headline-light {
    font-family: "Montserrat", sans-serif;
    font-weight: 300;
    font-size: 50px;
    fill: var(--text-light);
  }
  .headline-light .accent-italic { font-style: italic; font-weight: 400; }
  .headline-script {
    font-family: "Kaushan Script", cursive;
    font-size: 78px;
    font-weight: 400;
  }
  .phone-number {
    font-family: "Montserrat", sans-serif;
    font-weight: 700;
    font-size: 56px;
    fill: var(--ink);
  }
  .phone-tab { fill: var(--ink); }
  .phone-glyph { fill: none; stroke: var(--text-light); stroke-width: 3.5; stroke-linecap: round; }
</style>
</head>
<body>
  <svg class="billboard" viewBox="0 0 1280 630" xmlns="http://www.w3.org/2000/svg" aria-label="Limbwright Crew of Yuma billboard">
    <defs>
      <linearGradient id="green-sweep" x1="0" y1="0" x2="1" y2="0.6">
        <stop offset="0" stop-color="var(--green-deep)"/>
        <stop offset="1" stop-color="var(--green-bright)"/>
      </linearGradient>
      <linearGradient id="photo-tones" x1="0" y1="0" x2="1" y2="1">
        <stop offset="0" stop-color="var(--photo-tone-a)"/>
        <stop offset="1" stop-color="var(--photo-tone-b)"/>
      </linearGradient>
    </defs>

    <rect class="board-base" x="0" y="0" width="1280" height="630"/>

    <path class="green-field" fill="url(#green-sweep)"
          d="M0,0 L540,0 Q600,250 920,510 Q700,470 560,475 Q300,490 0,630 Z"/>

    <path class="landscape-photo" role="img" aria-label="Photo of a lone flat-topped tree on open grassland under a blue sky"
          fill="url(#photo-tones)"
          d="M592,0 L1280,0 L1280,625 Q1070,545 858,590 Q940,535 1060,495 Q760,390 680,210 Q640,100 592,0 Z"/>

    <text class="headline-light" x="60" y="240"><tspan class="headline-script">Artistic</tspan><tspan dx="14">thinning</tspan></text>
    <text class="headline-light" x="60" y="323">and shaping of <tspan class="headline-script" dx="4">trees</tspan></text>
    <text class="headline-light" x="60" y="392">in <tspan class="accent-italic">Arizona</tspan></text>

    <g class="phone-badge">
      <path class="phone-tab" d="M274,500 L328,500 L328,560 A27,27 0 0 1 274,560 Z"/>
      <circle class="phone-glyph" cx="301" cy="558" r="17"/>
      <path class="phone-glyph" d="M294,550 q-2,10 8,16 l4,-3 -4,-4 -3,2 q-3,-3 -4,-7 l2,-3 -3,-4 z"/>
    </g>
    <text class="phone-number" x="352" y="580">602-555-0147</text>
  </svg>
</body>
</html>
```